Business Card Design

I am after a business card design to be made for my pet care business in Darwin, Northern Territory Australia called Waggly Whiskers. I am a certified canine trainer and offer training classes from puppy love class, basic obedience classes, intermediate classes, private lessons, mobile dog wash and grooming and pet minding. I currently have a logo that I would like used on the card that incorporates different shades of orange with the writing in black. I really want my card to stand out from the rest and look professional, easy to read with 'the edge' factor. Im thinking both sides printed on with contact details on one side and services provided on the back
Updates

Thank you all so much for your time. I am overwhelmed with designs as they are all 

really great. My business partner and myself have shortlisted a few that really caught our eye and
Will update as soon as we decide. 

Once again thank you to you all for your great designs :)

Industry/Entity Type

Training

Contact Information for Business Card

Waggly Whiskers
wagglywhiskers@mailbox-example.com
wagglywhiskers-example.com.au
0487312645
pet minding
Puppy classes
basic obedience classes
intermediate obedience classes
private lessons
mobile dog wash and grooming
certified dog trainer
CTVB certified
Police checked
fully insured
honest
reliable
find us on SocialSite www.socialsite-example.com/wagglywhiskers

Requirements
Must have
• My current logo either the stacked version or side by side - whatever works best and must include my services

```html
<!DOCTYPE html>
<html lang="en">
<head>
<meta charset="utf-8">
<title>Waggly Whiskers – Business Card</title>
<link rel="stylesheet" href="https://fonts.googleapis.com/css2?family=Nunito:wght@800&family=Quicksand:wght@300&family=Dancing+Script:wght@400&family=Arimo:wght@700&display=swap">
<style>
  :root {
    --board: #d7d7d7;
    --label: #f26a1f;
    --orange: #ff6600;
    --amber: #f7931e;
    --black: #000000;
    --white: #ffffff;
    --ink: #222222;
    --gold: #d4a73a;
    --gold-light: #ecd9a8;
    --bronze: #8a6a2c;
  }
  html, body {
    margin: 0;
    padding: 0;
    width: 1077px;
    height: 1200px;
    overflow: hidden;
    background: var(--board);
  }
  .board {
    position: relative;
    width: 1077px;
    height: 1200px;
  }
  .side-label {
    position: absolute;
    left: 30px;
    margin: 0;
    font-family: "Nunito", sans-serif;
    font-weight: 800;
    font-size: 64px;
    line-height: 1;
    color: var(--label);
  }
  .side-label--front { top: 228px; }
  .side-label--back { top: 842px; left: 22px; }

  .card {
    position: absolute;
    left: 202px;
    width: 720px;
    height: 483px;
    overflow: hidden;
  }
  .card--front { top: 45px; }
  .card--back { top: 612px; background: var(--black); }

  /* Front */
  .pattern-band {
    position: absolute;
    inset: 0;
    background: linear-gradient(100deg, var(--orange), var(--black) 30%, var(--amber) 55%, var(--black) 80%, var(--orange));
  }
  .front-wave {
    position: absolute;
    inset: 0;
  }
  .logo-art {
    position: absolute;
    left: 4px;
    top: 105px;
    width: 234px;
    height: 258px;
    border-radius: 48% 52% 20% 30% / 40% 40% 20% 20%;
    background: radial-gradient(circle at 55% 30%, var(--gold) 0%, #dcb35a 55%, var(--gold-light) 100%);
  }
  .divider {
    position: absolute;
    left: 285px;
    top: 80px;
    width: 5px;
    height: 268px;
    background: var(--black);
  }
  .brand-name {
    position: absolute;
    left: 325px;
    top: 120px;
    margin: 0;
    font-family: "Quicksand", sans-serif;
    font-weight: 300;
    font-size: 40px;
    line-height: 50px;
    letter-spacing: 1px;
    color: var(--ink);
  }
  .tagline {
    position: absolute;
    left: 322px;
    top: 218px;
    margin: 0;
    font-family: "Dancing Script", cursive;
    font-size: 28px;
    color: var(--ink);
  }
  .contact {
    position: absolute;
    left: 352px;
    top: 271px;
    margin: 0;
    padding: 0;
    list-style: none;
    font-family: "Arimo", Arial, sans-serif;
    font-weight: 700;
    font-size: 18px;
    line-height: 27px;
    color: var(--black);
  }

  /* Back */
  .back-curve {
    position: absolute;
    inset: 0;
  }
  .logo-watermark {
    position: absolute;
    left: 280px;
    top: 14px;
    width: 380px;
    height: 470px;
    border-radius: 45% 40% 10% 20% / 30% 30% 5% 10%;
    background: linear-gradient(160deg, #9c7a32, var(--bronze) 60%, #a89a80);
    opacity: 0.85;
  }
  .services {
    position: absolute;
    left: 148px;
    top: 37px;
    margin: 0;
    font-family: "Arimo", Arial, sans-serif;
    font-weight: 700;
    font-size: 24px;
    line-height: 34.5px;
    color: var(--white);
    white-space: pre-line;
  }
  .social-bar {
    position: absolute;
    left: 108px;
    top: 366px;
    width: 500px;
    height: 36px;
    background: var(--orange);
  }
  .social-link {
    position: absolute;
    left: 40px;
    top: 0;
    margin: 0;
    font-family: "Arimo", Arial, sans-serif;
    font-weight: 700;
    font-size: 19px;
    line-height: 36px;
    color: var(--black);
  }
</style>
</head>
<body>
<main class="board">
  <p class="side-label side-label--front">front</p>
  <section class="card card--front">
    <div class="pattern-band" role="img" aria-label="Orange, amber and black chevron pattern bands"></div>
    <svg class="front-wave" viewBox="0 0 720 483" width="720" height="483" aria-hidden="true">
      <path d="M0 70 C 150 20, 300 110, 480 50 C 580 20, 660 15, 720 20 L 720 435 C 600 400, 480 430, 360 440 C 230 450, 120 400, 0 405 Z" fill="#ffffff"/>
    </svg>
    <div class="logo-art" role="img" aria-label="Logo artwork of dog, cat, bird and rabbit silhouettes in golden tones"></div>
    <div class="divider"></div>
    <h1 class="brand-name">WAGGLY<br>WHISKERS</h1>
    <p class="tagline">“It’s wonderful, to be waggly”</p>
    <ul class="contact">
      <li>wagglywhiskers@mailbox-example.com</li>
      <li>wagglywhiskers-example.com.au</li>
      <li>0487312645</li>
    </ul>
  </section>

  <p class="side-label side-label--back">back</p>
  <section class="card card--back">
    <svg class="back-curve" viewBox="0 0 720 483" width="720" height="483" aria-hidden="true">
      <path d="M0 0 L 68 0 C 20 80, 120 200, 112 285 C 105 360, 70 420, 70 483 L 0 483 Z" fill="#ff6600"/>
    </svg>
    <div class="logo-watermark" role="img" aria-label="Faint logo silhouettes of dog, cat, bird and rabbit"></div>
    <p class="services">I am a certified canine trainer and offer
training classes from puppy love class, basic
obedience classes, intermediate classes,
private lessons, mobile dog wash and
grooming and pet minding Puppy classes
private lessons mobile dog wash and
grooming certified dog trainer CTVB certified
Police checked fully insured honest reliable
find us on SocialSite</p>
    <div class="social-bar">
      <p class="social-link">www.socialsite-example.com/wagglywhiskers</p>
    </div>
  </section>
</main>
</body>
</html>
```